Flyer Rework for Accountants and Lawyers

Information flyer for accountants and lawyers. Text and flowchart provided. Just need to make it look presentable for print and email. Needs to add logo (AI file provided) and provide graphics. No more than two pages. Our corporate visual identify guidelines are attached (MUST Use). Completed on both AI file and PPTX file.
Target Market(s)
Accountants, Company Directors and Lawyers
Industry/Entity Type
Finance And Accounting
Requirements
Must have
- Our corporate visual identify guidelines are attached (MUST Use)

```html
<!DOCTYPE html>
<html lang="en">
<head>
<meta charset="utf-8">
<title>Fernbrook Advisory – Director Penalty Notices</title>
<link rel="stylesheet" href="https://fonts.googleapis.com/css2?family=Arimo:wght@400;700&display=swap">
<style>
  :root {
    --green: #6cbd45;
    --green-pale: #eef5e6;
    --grey-row: #efefef;
    --ink: #1e1e1e;
    --ink-soft: #555555;
    --bullet: #7a7a7a;
    --white: #ffffff;
  }
  * { box-sizing: border-box; margin: 0; padding: 0; }
  html, body { width: 848px; height: 1200px; overflow: hidden; background: var(--white); }
  body { font-family: "Arimo", Arial, sans-serif; color: var(--ink); }
  .flyer { position: relative; width: 848px; height: 1200px; overflow: hidden; background: var(--white); }

  .brand { position: absolute; left: 18px; top: 14px; display: flex; align-items: center; gap: 12px; }
  .brand-mark { width: 62px; height: 62px; border-radius: 50%; background: var(--green); }
  .brand-name { font-size: 27px; font-weight: 400; color: var(--green); letter-spacing: 0.5px; line-height: 1; }
  .brand-tagline { font-size: 14px; color: var(--ink-soft); margin-top: 4px; }

  .values {
    position: absolute; left: 185px; top: 111px; width: 478px; height: 54px;
    border: 4px solid var(--green); border-radius: 27px;
    display: flex; align-items: center; justify-content: center;
    font-size: 23px; font-weight: 700; color: var(--ink-soft); letter-spacing: 1px; word-spacing: 6px;
  }

  .intro { position: absolute; left: 28px; top: 198px; width: 792px; font-size: 18.5px; line-height: 1.42; }

  .section-tab { position: absolute; left: 26px; top: 296px; height: 40px; }
  .section-tab svg { position: absolute; left: 0; top: 0; }
  .section-tab span { position: relative; display: block; padding: 6px 0 0 12px; font-size: 24px; color: var(--white); }

  .lead { position: absolute; left: 28px; top: 348px; width: 792px; font-size: 18.5px; line-height: 1.4; text-align: justify; }

  .facts { position: absolute; left: 14px; top: 509px; width: 820px; border-collapse: separate; border-spacing: 0 4px; }
  .facts th {
    background: var(--green); color: var(--white); font-weight: 400; font-size: 25px;
    height: 32px; padding: 0; text-align: center;
  }
  .facts th + th { border-left: 3px solid var(--white); }
  .facts td { font-size: 18px; line-height: 1.4; vertical-align: top; padding: 10px 14px; }
  .facts td.fact { width: 250px; }
  .facts td.detail { border-left: 3px solid var(--white); }
  .facts tr.tone-green td { background: var(--green-pale); }
  .facts tr.tone-grey td { background: var(--grey-row); }
  .fact-num { display: inline-block; width: 22px; }
  .fact-indent { padding-left: 22px; display: block; }
  .options { list-style: none; margin-top: 6px; }
  .options li { position: relative; padding-left: 24px; margin-bottom: 2px; }
  .options li::before { content: ""; position: absolute; left: 2px; top: 6px; width: 12px; height: 12px; background: var(--bullet); }
  .row-middle td { vertical-align: middle; }

  .footer-band { position: absolute; left: 0; bottom: 0; width: 848px; height: 36px; background: var(--green); }
</style>
</head>
<body>
<main class="flyer">
  <header class="brand">
    <div class="brand-mark"></div>
    <div>
      <div class="brand-name">FERNBROOK ADVISORY</div>
      <div class="brand-tagline">Restructuring &amp; Solvency Accountants</div>
    </div>
  </header>

  <div class="values">INDEPENDENT CONCISE EFFICIENT</div>

  <p class="intro">Company directors and their advisors need to be aware that non-lodgement of Business Activities Statements (“BAS”) and Superannuation Guarantee Charge (“SCG”) Statements with the ATO may be personally liability for these debts.</p>

  <div class="section-tab">
    <svg width="390" height="40" viewBox="0 0 390 40" aria-hidden="true">
      <path d="M0 0 H372 L390 20 L372 40 H0 Z" fill="var(--green)"/>
    </svg>
    <span>Director Penalty Notices (“DPN”)</span>
  </div>

  <p class="lead">The ATO uses DPNs and Garnishee Notices to recovery tax debts and to impose positive obligations on Directors to deal with outstanding PAYG Withholding and the Superannuation Guarantee Charge debts (“Tax Debts”).<br>The DPN regime makes directors of companies who fail to pay Tax Debts personally liable. The key facts of DPN regime are outlined below:</p>

  <table class="facts">
    <thead>
      <tr><th>Facts</th><th>Key facts of a Directors Penalty Notice</th></tr>
    </thead>
    <tbody>
      <tr class="tone-green" style="height:73px">
        <td class="fact"><span class="fact-num">1.</span>Director personal<span class="fact-indent">liabilities</span></td>
        <td class="detail">Directors become personally liable for Tax Debts 21 days are the DPN Notice is issued</td>
      </tr>
      <tr class="tone-grey" style="height:92px">
        <td class="fact"><span class="fact-num">2.</span>Automatic liability for<span class="fact-indent">unreported and unpaid Tax Debts</span></td>
        <td class="detail">Where a company’s Tax Debts were both unreported and unpaid 3 months after the due date, the directors are automatically personally liable for the Tax Debts.</td>
      </tr>
      <tr class="tone-green" style="height:176px">
        <td class="fact"><span class="fact-num">3.</span>Avoiding personal<span class="fact-indent">liability for directors once they receive a DPN</span></td>
        <td class="detail">Within 21 days of issuing the DPN (which may be received a week or more after issue), a director can avoid personal liability by either:
          <ul class="options">
            <li>Paying the Tax Debt</li>
            <li>Appointing an Administrator to the company</li>
            <li>Appointing a Liquidator to the company.</li>
          </ul>
        </td>
      </tr>
      <tr class="tone-grey row-middle" style="height:80px">
        <td class="fact"><span class="fact-num">4.</span>Effect on new directors</td>
        <td class="detail">New directors are liable if outstanding Tax Debts are unpaid 30 days after their appointment as director</td>
      </tr>
      <tr class="tone-green row-middle" style="height:76px">
        <td class="fact"><span class="fact-num">5.</span>Time frames</td>
        <td class="detail">ATO can only enforce a DPN after 21 days of giving notice to the director and notice can be given to the company tax agent</td>
      </tr>
    </tbody>
  </table>

  <div class="footer-band" aria-hidden="true"></div>
</main>
</body>
</html>
```